Copper Hollow Sparkling

Hi all,

Thanks for taking the time to check out our brief.

Copper Hollow is an Australian wine company based in Victoria, and have been around for more than 20 years. We have a well-known sparkling Chardonnay Pinot Noir that needs a package revamp and we need your help!

Check out our current package here: http://www.copperhollowvino.com.au/our-wines/dsp-default_b.cfm?loadref=17

So here's the brief:

1. Use of the Copper Hollow logo (silhouette) and text mandatory - but can be as small/large as required.

2. Design must be shown on a sparkling bottle.

3. Can be closed with cork or crown seal - neck label/hood not mandatory.

4. Front label size to be no larger than 75mm high x 100mm wide. Back label to be no larger than 75mm x 100mm

5. Label does not have to be square/rectangular. Happy to see thoughts outside the box.

6. Design cannot be printed onto the bottle - must be on a label that can be applied to the bottle.

7. Be forward thinking. Be interesting. This design does not have to tie into our still (red and white) wine range.

8. Mandatory information to be shown on front label - a. Wine of Australia - b. Sparkling Chardonnay Pinot Noir

9. Mandatory info for front label - a. 750mL - b. Alcohol e.g. 13.5% ALC/VOL - c. Wine of Australi - d. Producer address (please insert dummy address at this stage - e. standard drinks e.g. approx 8.0 standard drinks (this can also be shown in the standard drinks glass logo) - f. space for a tasting blurb

10. Try to stay away from anything floral or overly girly.

Industry/Entity Type

Floral

Requirements
Must have
• Design must be shown on a sparkling wine bottle & include the full label design separately
Should not have
• Try to stay away from anything too floral and overly girly.

```html
<!DOCTYPE html>
<html lang="en">
<head>
<meta charset="utf-8">
<title>Copper Hollow Sparkling – Front Label</title>
<link rel="stylesheet" href="https://fonts.googleapis.com/css2?family=Raleway:wght@200;300&family=Cormorant+Garamond:wght@600&display=swap">
<style>
  :root {
    --page: #ffffff;
    --label-ground: #ad7060;
    --glass-top: #f3b3a7;
    --glass-bottom: #c48274;
    --glass-left: #fde0b6;
    --glass-right: #e1cba1;
    --glass-meet: #fbe6cc;
    --band: rgba(255, 247, 214, 0.86);
    --ink: #1e1714;
    --label-light: #f7d3be;
    --brand: #f6d9b2;
  }
  * { margin: 0; padding: 0; box-sizing: border-box; }
  html, body {
    width: 1200px;
    height: 1000px;
    overflow: hidden;
    background: var(--page);
  }
  .canvas {
    position: relative;
    width: 1200px;
    height: 1000px;
  }
  .front-label {
    position: absolute;
    left: 172px;
    top: 157px;
    width: 905px;
    height: 681px;
    background: var(--label-ground);
    overflow: hidden;
  }
  .glass-motif {
    position: absolute;
    left: 0;
    top: 0;
    width: 905px;
    height: 681px;
  }
  .title-band {
    position: absolute;
    left: 105px;
    top: 280px;
    width: 660px;
    height: 106px;
    background: var(--band);
    text-align: center;
    color: var(--ink);
    font-family: "Raleway", sans-serif;
  }
  .title-band .style {
    display: block;
    padding-top: 14px;
    font-weight: 300;
    font-size: 31px;
    letter-spacing: 0.04em;
    line-height: 1;
  }
  .title-band .varietal {
    display: block;
    margin-top: 6px;
    font-weight: 300;
    font-size: 48px;
    font-variant: small-caps;
    letter-spacing: 0.02em;
    line-height: 1;
  }
  .origin {
    position: absolute;
    left: 33px;
    top: 617px;
    font-family: "Raleway", sans-serif;
    font-weight: 200;
    font-size: 27px;
    color: var(--label-light);
  }
  .producer {
    position: absolute;
    right: 46px;
    top: 628px;
    font-family: "Cormorant Garamond", serif;
    font-weight: 600;
    font-size: 17px;
    letter-spacing: 0.38em;
    color: var(--brand);
  }
</style>
</head>
<body>
  <main class="canvas">
    <section class="front-label">
      <svg class="glass-motif" viewBox="0 0 905 681" role="img"
           aria-label="Four coupe glasses arranged in a cross, their stems meeting at the centre: pink above, rose below, peach to the left and gold to the right">
        <defs>
          <linearGradient id="vertical-glasses" x1="0" y1="0" x2="0" y2="1">
            <stop offset="0" stop-color="var(--glass-top)"/>
            <stop offset="0.5" stop-color="var(--glass-meet)"/>
            <stop offset="1" stop-color="var(--glass-bottom)"/>
          </linearGradient>
          <linearGradient id="horizontal-glasses" x1="0" y1="0" x2="1" y2="0">
            <stop offset="0" stop-color="var(--glass-left)"/>
            <stop offset="0.5" stop-color="var(--glass-meet)"/>
            <stop offset="1" stop-color="var(--glass-right)"/>
          </linearGradient>
        </defs>
        <rect x="275" y="6" width="318" height="660" fill="url(#vertical-glasses)"/>
        <rect x="105" y="178" width="660" height="318" fill="url(#horizontal-glasses)"/>
      </svg>

      <h1 class="title-band">
        <span class="style">SPARKLING</span>
        <span class="varietal">Chardonnay Pinot Noir</span>
      </h1>

      <p class="origin">Wine of Australia</p>
      <p class="producer">COPPER HOLLOW</p>
    </section>
  </main>
</body>
</html>
```